依頼詳細
拠点周辺での新規顧客の獲得及び新拠点の営業開始の為、新聞折込を計画しており、新聞折込用のチラシ製作をお願い致します。お手入れできていないお庭をなんとかしたい!と思っている方、ご自分でお手入れしているもののやはりプロに頼みたい!と思っている方の目に留まるデザインを希望しております。ご相談を受け、現地で状態をしっかり確認した後ご提案、お見積りさせて頂く為、価格や料金プランはございません。また、新拠点の営業期間は当面3月〜5月の予定です。
記載項目
社  名:樋口庭苑
営業拠点:長野本店、茅野新店※3月〜5月
受付時間:9:30〜18:30 ※年中無休
電話番号:026-318-4452
(携帯 :090-7723-6041)
E- m a i l:info@hgchteien-example.com
本店住所:長野市若葉台西2丁目4-7 コーポ白樺105
サイズ
A4
ページ数
片面
希望イメージ
シンプル 複雑
単色 カラフル
暗い 明るい
日常 高級
遊び心 厳粛
未来的 伝統的
女性的 男性的
希望する色
緑系、水色系
納品ファイル
• 高解像度JPG (.jpg)
補足説明
◾️依頼タイトル変更
◾️施工例などの写真は使用しません。
一目で『業者のチラシ』と分かるものとは一線を画し、
「これ植木屋さん?!」と意表を突くデザイン性に富んだチラシを求めております。
抽象的で申し訳ないのですが、お力添えをお願い致します。

◾️記載項目の事業者情報の他、下記の記載をお願い致します。
・グリーンアドバイザーがお庭をなんとかしたい方のお悩みに丁寧にお応えする、という趣旨
・ご相談、お見積りは無料であること
・茅野市(長野県)で営業を開始すること※営業期間は3月から5月
◾️他社様ですが、素人なりに製作した過去のサンプルを添付しました。
*誠に申し訳ございませんが、
『概要・特徴』の内容を誤っておりました。
1級技能士と記載しておりますが、
造園関連ではございませんでした。
本当に申し訳ございません。
ご迷惑をおかけいたしますが、
記載項目からは外していただきますよう、
何卒お願い申し上げます。
■新聞折込は長野市内の部数を多めに予定しておりますので、
茅野新店についての記載は目立つ配置でなくて良いです。
*ご提案いただける方の制限につきまして、
訂正させていただいております。
多くの皆様のご提案をお待ちしております!
*前回同様
■ 選んだ理由

これ、植木屋さんなんだー!と驚くなんとも清潔感のある斬新さと、読みやすく分かりやすいシンプルさがとても印象的で、この度選ばせて頂きました。

■ 提案者全員のお礼・コメント

この度は、当方のご依頼にこのように多くの皆様にご提案をいただき、ただただ感謝申し上げます。利用させていただくのが初めてで、ご説明不足や当方の不手際等で大変お手数をおかけしてしまったにも関わらず、皆様のご対応の迅速さに、脱帽でした。本当に、有難うございました。

```html
<!DOCTYPE html>
<html lang="ja">
<head>
<meta charset="utf-8">
<title>樋口庭苑 庭木のお手入れ</title>
<link rel="stylesheet" href="https://fonts.googleapis.com/css2?family=Noto+Sans+JP:wght@500;700;900&display=swap">
<style>
:root{
  --yellow:#f3d31c;
  --yellow-deep:#e6bf0c;
  --green-dark:#1d6b2c;
  --green:#2f8a34;
  --green-light:#7dbb3c;
  --red:#e0261c;
  --white:#ffffff;
  --ink:#2c3a2c;
  --panel:#fbfbf4;
}
*{box-sizing:border-box;margin:0;padding:0}
html,body{width:851px;height:1200px;overflow:hidden}
body{font-family:"Noto Sans JP",sans-serif;color:var(--green-dark);background:var(--white)}
.flyer{position:relative;width:851px;height:1200px;overflow:hidden}
.backdrop{position:absolute;inset:0 0 238px 0;
  background:linear-gradient(90deg,var(--yellow) 0 20%,var(--yellow-deep) 20% 20.4%,var(--yellow) 20.4% 40%,var(--yellow-deep) 40% 40.4%,var(--yellow) 40.4% 60%,var(--yellow-deep) 60% 60.4%,var(--yellow) 60.4% 80%,var(--yellow-deep) 80% 80.4%,var(--yellow) 80.4%)}
.headline{position:absolute;left:0;right:0;top:22px;text-align:center;font-weight:900;font-size:84px;line-height:96px;color:var(--green-dark);
  text-shadow:0 0 6px var(--white),3px 3px 0 var(--white),-3px -3px 0 var(--white),3px -3px 0 var(--white),-3px 3px 0 var(--white)}
.headline .small{font-size:64px}
.advisor-photo{position:absolute;left:86px;top:262px;width:150px;height:150px;border-radius:50%;background:radial-gradient(circle at 50% 40%,#f1efe9,#c9c6bf);border:4px solid var(--white)}
.advisor-band{position:absolute;left:258px;top:290px;width:563px;height:42px;background:var(--green-dark);color:var(--white);font-weight:900;font-size:30px;line-height:42px;padding-left:22px;letter-spacing:1px}
.promise{position:absolute;left:258px;top:340px;font-weight:900;font-size:32px;line-height:44px;color:var(--green)}
.services{position:absolute;left:88px;list-style:none;font-weight:700;font-size:23px;line-height:33px;color:var(--green-dark)}
.services li::before{content:"";display:inline-block;width:12px;height:12px;border-radius:50%;background:var(--green-light);margin-right:9px;vertical-align:2px}
.services.care{top:448px}
.services.prune{top:562px}
.one-tree{position:absolute;left:84px;top:672px;width:262px;height:42px;background:var(--green-dark);color:var(--white);font-weight:900;font-size:21px;line-height:42px;text-align:center}
.free{position:absolute;top:750px;width:130px;height:130px;border-radius:50%;background:var(--red);color:var(--white);font-weight:900;text-align:center;display:flex;flex-direction:column;justify-content:center;border:4px solid var(--white)}
.free .what{font-size:21px;line-height:28px}
.free .price{font-size:34px;line-height:42px}
.free.consult{left:82px}
.free.quote{left:220px}
.tools{position:absolute;left:380px;top:430px;width:440px;height:532px;border-radius:20px 20px 0 0;
  background:linear-gradient(160deg,rgba(255,255,255,.25),rgba(210,60,30,.35) 60%,rgba(200,40,30,.55))}
.chino{position:absolute;left:0;right:0;top:962px;height:40px;background:var(--white);padding-left:86px;font-weight:900;font-size:23px;line-height:40px;color:var(--green)}
.chino small{font-size:14px;font-weight:700;margin-left:12px;color:var(--green-dark)}
.footer{position:absolute;left:0;right:0;top:1002px;height:182px;background:var(--panel);padding:10px 86px 0}
.brand{display:flex;align-items:baseline;gap:16px;border-bottom:2px solid var(--green-light);padding-bottom:6px;line-height:44px}
.brand .name{font-weight:900;font-size:32px;color:var(--green-dark);letter-spacing:3px}
.brand .bases{font-size:14px;font-weight:500;color:var(--ink)}
.address{font-size:14px;line-height:22px;color:var(--ink);margin-top:8px;font-weight:500}
.contacts{display:flex;align-items:center;gap:22px;margin-top:6px;font-size:18px;line-height:26px;font-weight:700;color:var(--ink)}
.contacts span{display:flex;align-items:center;gap:6px}
.contacts svg{width:20px;height:20px;fill:var(--green)}
.contacts .hours{font-size:14px;font-weight:500}
.closing{position:absolute;left:0;right:0;bottom:0;height:16px;background:var(--green)}
</style>
</head>
<body>
<main class="flyer">
  <div class="backdrop" role="img" aria-label="黄色い木の板の背景"></div>

  <h1 class="headline">庭木<span class="small">の</span>お手入れ<br>できてますか?</h1>

  <div class="advisor-photo" role="img" aria-label="スーツ姿のグリーンアドバイザーの写真"></div>
  <div class="advisor-band">グリーンアドバイザーが</div>
  <p class="promise">お庭をなんとかしたい方の<br>お悩みをすっきり解決!!</p>

  <ul class="services care">
    <li>生垣の刈込</li>
    <li>植木の植え替え</li>
    <li>消毒作業</li>
  </ul>
  <ul class="services prune">
    <li>伸びた枝の剪定</li>
    <li>枝おろし</li>
    <li>高い木の伐採</li>
  </ul>
  <div class="one-tree">植木1本から剪定します!</div>

  <div class="free consult"><span class="what">ご相談</span><span class="price">無料</span></div>
  <div class="free quote"><span class="what">お見積り</span><span class="price">無料</span></div>

  <div class="tools" role="img" aria-label="赤い鉢に入ったスコップ・熊手など園芸道具の写真"></div>

  <p class="chino">茅野市(長野県)で営業スタート!!<small>※営業期間は3月〜5月</small></p>

  <footer class="footer">
    <div class="brand">
      <span class="name">樋口庭苑</span>
      <span class="bases">(営業拠点:長野本店、茅野新店 ※3月〜5月)</span>
    </div>
    <p class="address">〒380-0928 長野市若葉台西2丁目4-7 コーポ白樺105(本店)</p>
    <div class="contacts">
      <span><svg viewBox="0 0 24 24"><path d="M6.6 10.8a15 15 0 0 0 6.6 6.6l2.2-2.2c.3-.3.7-.4 1-.2 1.1.4 2.3.6 3.6.6.6 0 1 .4 1 1V20c0 .6-.4 1-1 1A17 17 0 0 1 3 4c0-.6.4-1 1-1h3.5c.6 0 1 .4 1 1 0 1.3.2 2.5.6 3.6.1.3 0 .7-.2 1z"/></svg>026-318-4452</span>
      <span><svg viewBox="0 0 24 24"><path d="M7 2h10a2 2 0 0 1 2 2v16a2 2 0 0 1-2 2H7a2 2 0 0 1-2-2V4a2 2 0 0 1 2-2zm0 3v13h10V5zm5 14.2a1 1 0 1 0 0 2 1 1 0 0 0 0-2z"/></svg>090-7723-6041</span>
      <span class="hours">9:30〜18:30 ※年中無休</span>
    </div>
    <div class="contacts">
      <span><svg viewBox="0 0 24 24"><path d="M3 5h18a1 1 0 0 1 1 1v12a1 1 0 0 1-1 1H3a1 1 0 0 1-1-1V6a1 1 0 0 1 1-1zm1 2.3V17h16V7.3l-8 5.2z"/></svg>info@hgchteien-example.com</span>
    </div>
  </footer>
  <div class="closing"></div>
</main>
</body>
</html>
```